Business card for our start up Automotive Shop

Clean business card design for our new automotive shop Brightline Motor Works. This card will be the template for all of our staff member including technicians and service advisors.

Brightline Motor Works is an automotive service shop catering to US domestic and asian import vehicles. We are a service and maintenance full service facility. Our aim is to provide the best quality workmanship and the best customer service experience in our industry.

Our target market are young professionals to people with families. We are not targeting a younger audience or the car modification scene. The card should be appealing to women of the 30+ age demographic.

We are a shop of younger professionals instead of an older crowd. The card design should reflect as such.

Target Market(s)

30+ Female demographic and 30+ male.

Industry/Entity Type

Automotive

Contact Information for Business Card

Must be clean and appealing to clients. Large enough and easy to read print.

Font styles to use
Sans Serif

Colors
f78f20
ffffff
b2b2b2
dddddd

Requirements
Must have
• Address, website and phone number
• 42-15 58th Ave
• Cedar Hollow NY 11462
• (718) 402-3917
• brightlinemotorworks.com
• There must be an area to add a Name and e-mail address for personalization purposes.
Nice to have
• Back of the card should have website.
• I would also like to incorporate yelp, google+, Facebook, and instagram widgets. Will add the exact pages but everything can be @ or / brightlinemotorworks
• That can be added on the back of the card.

```html
<!DOCTYPE html>
<html lang="en">
<head>
<meta charset="utf-8">
<title>Brightline Motor Works – Business Card</title>
<link href="https://fonts.googleapis.com/css2?family=Open+Sans:wght@400;600;700&display=swap" rel="stylesheet">
<style>
  :root {
    --brand-orange: #f78f20;
    --white: #ffffff;
    --silver: #dddddd;
    --silver-dark: #b2b2b2;
    --backdrop: #ececec;
  }
  * { margin: 0; padding: 0; box-sizing: border-box; }
  html, body {
    width: 1200px; height: 900px; overflow: hidden;
    background: var(--backdrop);
    font-family: "Open Sans", sans-serif;
  }
  .business-card {
    position: absolute;
    left: 150px; top: 172px;
    width: 900px; height: 556px;
    background: var(--brand-orange);
    color: var(--white);
    box-shadow: 0 10px 30px rgba(0,0,0,0.15);
  }
  .contact-block { position: absolute; left: 40px; }
  .person-name {
    top: 52px; font-size: 29px; font-weight: 700; letter-spacing: 0.3px;
  }
  .person-title { top: 92px; font-size: 22px; font-weight: 400; }
  .address { top: 150px; font-size: 22px; line-height: 33px; }
  .social-list, .contact-list { list-style: none; font-size: 21px; }
  .social-list { top: 236px; }
  .social-list li { display: flex; align-items: center; height: 39px; }
  .social-dot {
    width: 26px; height: 26px; border-radius: 50%;
    background: var(--white); margin-right: 13px; flex: none;
  }
  .contact-list { top: 396px; }
  .contact-list li { display: flex; align-items: center; height: 33px; }
  .contact-icon { width: 18px; height: 18px; margin-right: 14px; flex: none; }
  .brand-seal {
    position: absolute;
    left: 401px; top: 42px;
    width: 474px; height: 474px; border-radius: 50%;
    background: radial-gradient(circle at 40% 35%, #f4f4f4 0%, var(--silver) 60%, #cfcfcf 100%);
    display: flex; flex-direction: column; align-items: center; justify-content: center;
  }
  .brand-name {
    color: var(--brand-orange);
    font-weight: 700;
    text-align: center;
    line-height: 1.1;
  }
  .brand-name .line-main { display: block; font-size: 58px; letter-spacing: 2px; }
  .brand-name .line-sub { display: block; font-size: 32px; letter-spacing: 10px; margin-top: 6px; }
</style>
</head>
<body>
  <div class="business-card">
    <div class="contact-block person-name">DANIEL REYES</div>
    <div class="contact-block person-title">Managing Director</div>
    <div class="contact-block address">
      <div>42-15 58th Ave</div>
      <div>Cedar Hollow NY 11462</div>
    </div>

    <ul class="contact-block social-list">
      <li><span class="social-dot"></span>@brightlinemotorworks</li>
      <li><span class="social-dot"></span>@brightlinemotorworks</li>
      <li><span class="social-dot"></span>@brightlinemotorworks</li>
    </ul>

    <ul class="contact-block contact-list">
      <li>
        <svg class="contact-icon" viewBox="0 0 24 24" aria-hidden="true"><path fill="#fff" d="M6.6 10.8a15.2 15.2 0 0 0 6.6 6.6l2.2-2.2c.3-.3.7-.4 1-.2 1.1.4 2.3.6 3.6.6.6 0 1 .4 1 1V20c0 .6-.4 1-1 1A17 17 0 0 1 3 4c0-.6.4-1 1-1h3.5c.6 0 1 .4 1 1 0 1.3.2 2.5.6 3.6.1.3 0 .7-.2 1l-2.3 2.2z"/></svg>
        (718) 402-3917
      </li>
      <li>
        <svg class="contact-icon" viewBox="0 0 24 24" aria-hidden="true"><rect x="2" y="5" width="20" height="14" fill="#fff"/><path d="M2 5l10 8 10-8" fill="none" stroke="#f78f20" stroke-width="1.8"/></svg>
        info@brightlinemotorworks.com
      </li>
      <li>
        <svg class="contact-icon" viewBox="0 0 24 24" aria-hidden="true"><circle cx="12" cy="12" r="10" fill="#fff"/><path d="M2 12h20M12 2c3 3 3 17 0 20M12 2c-3 3-3 17 0 20" fill="none" stroke="#f78f20" stroke-width="1.5"/></svg>
        www.brightlinemotorworks.com
      </li>
    </ul>

    <div class="brand-seal">
      <div class="brand-name">
        <span class="line-main">BRIGHTLINE</span>
        <span class="line-sub">MOTOR WORKS</span>
      </div>
    </div>
  </div>
</body>
</html>
```